The Timber Loft

We need a business card design for our wardrobe company.
Please visit our website www.zorvelcabinets.com to get an idea of who we are.

```html
<!DOCTYPE html>
<html lang="en">
<head>
<meta charset="utf-8">
<title>The Timber Loft – Business Card</title>
<link rel="stylesheet" href="https://fonts.googleapis.com/css2?family=Poppins:wght@300;400;500;600&display=swap">
<style>
  :root {
    --backdrop: #8b8b8b;
    --card: #f4f3ef;
    --gold: #8c744a;
    --ink: #1c1c1c;
    --muted: #9a9a9a;
  }
  * { margin: 0; padding: 0; box-sizing: border-box; }
  html, body {
    width: 1200px; height: 904px; overflow: hidden;
    background: var(--backdrop);
    font-family: "Poppins", sans-serif;
  }
  .card {
    position: absolute; left: 400px; top: 52px;
    width: 400px; height: 800px;
    background: var(--card);
  }
  .card-frame {
    position: absolute; inset: 12px;
    border: 2px solid var(--gold);
  }
  .brand {
    position: absolute; left: 38px; top: 52px;
    display: flex; align-items: center; gap: 14px;
  }
  .brand-square {
    width: 64px; height: 64px;
    border: 2px solid var(--ink);
  }
  .brand-name {
    font-size: 15px; font-weight: 500; color: var(--ink);
    letter-spacing: 0.2px; line-height: 1.3;
  }
  .brand-tagline {
    font-size: 13px; font-weight: 500; color: var(--ink);
    line-height: 1.3;
  }
  .details {
    position: absolute; left: 0; right: 0; top: 175px;
    display: flex; flex-direction: column; align-items: center;
    text-align: center;
  }
  .icon { width: 16px; height: 16px; fill: var(--gold); display: block; }
  .person-name {
    margin-top: 12px;
    font-size: 27px; font-weight: 500; color: var(--gold);
    letter-spacing: 0.5px; line-height: 1.1;
  }
  .person-title {
    font-size: 16px; font-weight: 300; color: var(--muted);
  }
  .item { margin-top: 42px; display: flex; flex-direction: column; align-items: center; }
  .item-text {
    margin-top: 12px;
    font-size: 15px; font-weight: 300; color: var(--ink); line-height: 1.35;
  }
</style>
</head>
<body>
  <main class="card">
    <div class="card-frame"></div>

    <header class="brand">
      <div class="brand-square"></div>
      <div class="brand-text">
        <p class="brand-name">THE TIMBER LOFT</p>
        <p class="brand-tagline">Built Right, Made to Last</p>
      </div>
    </header>

    <section class="details">
      <svg class="icon" viewBox="0 0 16 16" aria-hidden="true"><circle cx="8" cy="4.5" r="3.5"/><path d="M1 16c0-4 3-6.5 7-6.5s7 2.5 7 6.5z"/></svg>
      <p class="person-name">DANIEL HART</p>
      <p class="person-title">President</p>

      <div class="item">
        <svg class="icon" viewBox="0 0 16 16" aria-hidden="true"><path d="M8 0a5.5 5.5 0 0 0-5.5 5.5C2.5 10 8 16 8 16s5.5-6 5.5-10.5A5.5 5.5 0 0 0 8 0zm0 7.7a2.2 2.2 0 1 1 0-4.4 2.2 2.2 0 0 1 0 4.4z"/></svg>
        <p class="item-text">Larkspur House, 42 Millbrook Lane<br>London N4 7QT</p>
      </div>

      <div class="item">
        <svg class="icon" viewBox="0 0 16 16" aria-hidden="true"><path d="M3.6 1l2.2 3.3-1.5 1.6c.9 2 2.6 3.8 4.8 4.8l1.6-1.5L14 11.4 12.6 14C6.5 14 2 9.5 2 3.4z"/></svg>
        <p class="item-text">020 7946 0183</p>
      </div>

      <div class="item">
        <svg class="icon" viewBox="0 0 16 16" aria-hidden="true"><path d="M1 3h14v10H1z" opacity="0.9"/><path d="M1 3l7 5.5L15 3" fill="none" stroke="#f4f3ef" stroke-width="1.2"/></svg>
        <p class="item-text">info@zorvelcabinets.com</p>
      </div>

      <div class="item">
        <svg class="icon" viewBox="0 0 16 16" aria-hidden="true"><circle cx="8" cy="8" r="7.5"/><path d="M0.5 8h15M8 0.5c-3 3.5-3 11.5 0 15M8 0.5c3 3.5 3 11.5 0 15" fill="none" stroke="#f4f3ef" stroke-width="1"/></svg>
        <p class="item-text">www.zorvelcabinets.com</p>
      </div>
    </section>
  </main>
</body>
</html>
```